Construction Contractor
Bayt Nuwaris
Professional
Fahad Omar Qurashi
Owner
Rawda Street P.O.Box 483920 Jeddah 24719 Saudi Arabia
baytnuwaris@mailbox-example.com
We need Logo to be in the middle and company name under the logo

```html
<!DOCTYPE html>
<html lang="en">
<head>
<meta charset="UTF-8">
<title>Bayt Nuwaris — Business Card</title>
<link href="https://fonts.googleapis.com/css2?family=Montserrat:wght@800&family=Open+Sans:wght@400;600&display=swap" rel="stylesheet">
<style>
  :root {
    --brown: #4a2e1c;
    --gold: #bfa068;
    --gold-light: #d9c392;
    --ink: #3a3a3a;
    --muted: #7a7a7a;
    --paper: #ffffff;
    --backdrop: #dcdcdc;
    --rule: #cfcfcf;
  }
  * { margin: 0; padding: 0; box-sizing: border-box; }
  html, body { width: 1200px; height: 984px; overflow: hidden; }
  body {
    background: var(--backdrop);
    font-family: "Open Sans", sans-serif;
    position: relative;
  }
  .card {
    position: absolute;
    left: 200px;
    width: 800px;
    height: 440px;
    background: var(--paper);
    border-radius: 26px;
    overflow: hidden;
    box-shadow: 0 10px 30px rgba(0,0,0,0.18);
  }
  .card-front { top: 40px; }
  .card-back { top: 504px; }

  .brand {
    position: absolute;
    display: flex;
    flex-direction: column;
    align-items: center;
    font-family: "Montserrat", sans-serif;
    font-weight: 800;
    color: var(--brown);
    letter-spacing: 1px;
    text-transform: uppercase;
    white-space: nowrap;
    line-height: 1.1;
  }
  .brand-mark {
    background: var(--gold);
    flex: none;
  }

  .card-front .brand {
    left: 50%;
    top: 50%;
    transform: translate(-50%, -50%);
    gap: 22px;
    font-size: 44px;
  }
  .card-front .brand-mark { width: 110px; height: 110px; }

  .swoosh { position: absolute; left: 0; bottom: 0; }

  .card-back .brand {
    left: 235px;
    top: 70px;
    transform: translateX(-50%);
    gap: 14px;
    font-size: 32px;
  }
  .card-back .brand-mark { width: 76px; height: 76px; }

  .divider {
    position: absolute;
    left: 470px;
    top: 100px;
    width: 1px;
    height: 240px;
    background: var(--rule);
  }
  .contact {
    position: absolute;
    left: 486px;
    top: 100px;
  }
  .person-name { font-size: 20px; font-weight: 600; color: var(--ink); }
  .person-role { font-size: 13px; color: var(--muted); margin-bottom: 40px; }
  .details { list-style: none; }
  .details li {
    display: flex;
    align-items: center;
    gap: 9px;
    font-size: 12.5px;
    color: var(--ink);
    line-height: 22px;
    white-space: nowrap;
  }
  .icon {
    width: 15px; height: 15px;
    border-radius: 50%;
    background: var(--ink);
    display: flex; align-items: center; justify-content: center;
    flex: none;
  }
  .icon svg { width: 9px; height: 9px; fill: var(--paper); }
</style>
</head>
<body>

<section class="card card-front">
  <div class="brand"><span class="brand-mark"></span>Bayt Nuwaris</div>
</section>

<section class="card card-back">
  <svg class="swoosh" width="800" height="440" viewBox="0 0 800 440">
    <path d="M0 300 C150 250 280 280 470 440 L0 440 Z" fill="var(--brown)"/>
    <path d="M0 330 C170 290 300 330 430 440 L330 440 C250 370 130 350 0 370 Z" fill="var(--gold)"/>
    <path d="M0 380 C120 370 220 390 290 440 L0 440 Z" fill="var(--brown)"/>
    <path d="M0 265 C200 230 380 290 560 440 L540 440 C380 305 210 250 0 282 Z" fill="var(--gold-light)"/>
  </svg>

  <div class="brand"><span class="brand-mark"></span>Bayt Nuwaris</div>

  <div class="divider"></div>

  <div class="contact">
    <p class="person-name">Fahad Omar Qurashi</p>
    <p class="person-role">Owner</p>
    <ul class="details">
      <li><span class="icon"><svg viewBox="0 0 10 10"><path d="M5 0a3.3 3.3 0 0 0-3.3 3.3C1.7 5.8 5 10 5 10s3.3-4.2 3.3-6.7A3.3 3.3 0 0 0 5 0zm0 4.6a1.3 1.3 0 1 1 0-2.6 1.3 1.3 0 0 1 0 2.6z"/></svg></span>Rawda Street P.O.Box 483920</li>
      <li><span class="icon"><svg viewBox="0 0 10 10"><path d="M5 0a3.3 3.3 0 0 0-3.3 3.3C1.7 5.8 5 10 5 10s3.3-4.2 3.3-6.7A3.3 3.3 0 0 0 5 0z"/></svg></span>Jeddah 24719 Saudi Arabia</li>
      <li><span class="icon"><svg viewBox="0 0 10 10"><path d="M2 .5 3.6 2.6 2.8 3.8c.7 1.5 1.9 2.7 3.4 3.4l1.2-.8L9.5 8 8.4 9.5C4.3 9.3.7 5.7.5 1.6z"/></svg></span>+966 12 555 0147</li>
      <li><span class="icon"><svg viewBox="0 0 10 10"><rect x="2.5" y="0.5" width="5" height="9" rx="1"/></svg></span>+966 55 555 0193</li>
      <li><span class="icon"><svg viewBox="0 0 10 10"><path d="M1 2h8v6H1z"/></svg></span>baytnuwaris@mailbox-example.com</li>
      <li><span class="icon"><svg viewBox="0 0 10 10"><circle cx="5" cy="5" r="3.5"/></svg></span>www.baytnuwaris.example</li>
    </ul>
  </div>
</section>

</body>
</html>
```